Website design for commercial and residential security company

we're looking to see some new designs for an established company with no website.

homepage and one inner page

here is a link to the homepage content, sitemap, logo and more.
https://files.brontavel.net/share/7QxmPzLrTw2vNkdJhYcsa9eFgbUoiVwRn?view=open

call to action should be Request A Quote

if you have any questions please send them to us asap

thank you

1 page

Sans Serif

```html
<!DOCTYPE html>
<html lang="en">
<head>
<meta charset="utf-8">
<title>Halden Ridge Security — Security with Smart Tools</title>
<link href="https://fonts.googleapis.com/css2?family=Poppins:wght@300;400;500;600;700&display=swap" rel="stylesheet">
<style>
:root{
  --gold:#d1ad3a;
  --ink:#1c1c1c;
  --dark:#1e1e1e;
  --light:#f2f2f2;
  --white:#ffffff;
  --muted:#9a9a9a;
}
*{margin:0;padding:0;box-sizing:border-box}
html,body{width:1200px;height:3918px;overflow:hidden}
body{font-family:"Poppins",sans-serif;color:var(--ink);background:var(--white);position:relative}
.abs{position:absolute}
a{color:inherit;text-decoration:none}

/* hero */
.hero{left:0;top:0;width:1200px;height:800px;background:linear-gradient(160deg,#3a3630 0%,#1b1a18 45%,#2b2a28 75%,#121212 100%)}
.hero-photo{left:0;top:0;width:1200px;height:800px;background:radial-gradient(ellipse at 62% 30%,rgba(190,180,160,.35),transparent 40%),linear-gradient(90deg,rgba(0,0,0,.45),rgba(0,0,0,.1))}
.brand{display:flex;align-items:center;gap:10px;font-weight:600;color:var(--white);font-size:26px;letter-spacing:.5px;white-space:nowrap}
.brand-dot{width:14px;height:14px;border-radius:50%;background:var(--gold)}
.nav-link{position:absolute;top:75px;color:var(--white);font-size:14px;font-weight:500;white-space:nowrap}
.btn-gold{background:var(--gold);color:var(--white);font-weight:500;font-size:14px;display:flex;align-items:center;justify-content:center;letter-spacing:.5px}
.btn-outline{border:1.5px solid currentColor;font-weight:600;font-size:14px;display:flex;align-items:center;justify-content:center;letter-spacing:.5px;white-space:nowrap}
.btn-dark{background:var(--ink);color:var(--white);font-size:12px;font-weight:500;display:flex;align-items:center;justify-content:center;letter-spacing:.4px}
.hero-sub{left:93px;top:305px;color:var(--white);font-size:19px;font-weight:300}
.hero-title{left:93px;top:347px;color:var(--white);font-size:60px;font-weight:500;line-height:68px;white-space:nowrap}
.hero-title strong{color:var(--gold);font-weight:700;display:block}
.hero-rule{left:665px;top:457px;width:535px;height:2px;background:var(--gold)}

/* mission */
.watermark{left:160px;top:1322px;font-size:120px;font-weight:500;color:#f6f6f6;white-space:nowrap;line-height:140px;letter-spacing:2px}
.mission-bar{left:205px;top:853px;width:82px;height:496px;background:var(--gold)}
.camera{left:0;top:915px;width:456px;height:300px;border-radius:0 150px 150px 0;background:linear-gradient(160deg,#ffffff 0%,#eceef0 45%,#cfd2d5 100%)}
.pointer{left:371px;top:1099px;width:210px;height:2px;background:var(--gold)}
.pointer-dot{left:364px;top:1092px;width:16px;height:16px;border-radius:50%;background:var(--white)}
.mission{left:616px;top:915px;width:470px}
.mission h2{font-size:42px;font-weight:500;margin-bottom:30px}
.mission h2 span{color:var(--gold)}
.mission .lead{font-size:15px;font-weight:600;line-height:30px;margin-bottom:24px}
.mission .body{font-size:15px;line-height:30px;margin-bottom:34px}

/* solutions */
.solutions{left:0;top:1443px;width:1200px;height:1703px;background:var(--light)}
.card{left:93px;width:1017px;height:524px;overflow:hidden;background:#1d1d1d}
.card-photo{position:absolute;left:0;top:0;width:100%;height:100%}
.card-copy{position:absolute;left:61px;width:460px;color:var(--white)}
.card-copy h3{font-size:42px;font-weight:500;margin-bottom:40px;white-space:nowrap}
.card-copy .tag{color:var(--gold);font-size:20px;font-weight:500;line-height:30px;margin-bottom:8px;width:450px}
.card-copy p{font-size:15px;line-height:30px}
.card .btn-dark{position:absolute;left:841px;width:128px;height:42px}

/* cta */
.cta{left:0;top:3146px;width:1200px;height:400px;background:#fafbfb}
.cta-photo{left:560px;top:3146px;width:640px;height:400px;background:linear-gradient(100deg,rgba(250,251,251,1) 0%,rgba(230,234,236,.8) 30%,#cfd6da 65%,#b9c3c8 100%)}
.cta-title{left:93px;top:3255px;font-size:34px;font-weight:500;white-space:nowrap}
.cta-text{left:93px;top:3305px;width:460px;font-size:15px;line-height:30px}

/* footer */
.footer{left:0;top:3546px;width:1200px;height:372px;background:var(--dark)}
.foot-col{top:3704px;color:var(--white)}
.foot-col h4{font-size:15px;font-weight:500;margin-bottom:12px}
.foot-col li{list-style:none;color:var(--muted);font-size:15px;line-height:35px;display:flex;align-items:center;gap:6px;white-space:nowrap}
.copyright{left:113px;top:3848px;font-size:11px;color:#6c6c6c}
</style>
</head>
<body>

<!-- HERO -->
<section class="abs hero"></section>
<div class="abs hero-photo" role="img" aria-label="Photo of a security camera mounted on a pole in front of a dark building facade"></div>
<div class="abs brand" style="left:93px;top:62px"><span class="brand-dot"></span>Halden Ridge</div>
<nav>
  <a class="nav-link" style="left:566px">ABOUT</a>
  <a class="nav-link" style="left:663px">SOLUTIONS
    <svg width="10" height="8" viewBox="0 0 10 8" style="margin-left:3px"><path d="M1 2l4 4 4-4" stroke="#fff" stroke-width="1.6" fill="none"/></svg></a>
  <a class="nav-link" style="left:806px">RESOURCES</a>
</nav>
<a class="abs btn-gold" style="left:970px;top:61px;width:140px;height:46px">CONTACT</a>
<p class="abs hero-sub">SUBTITLE HERE</p>
<h1 class="abs hero-title">Ensuring security<strong>with smart tools.</strong></h1>
<div class="abs hero-rule"></div>
<a class="abs btn-outline" style="left:93px;top:528px;width:193px;height:47px;color:#fff">REQUEST&nbsp; A QUOTE</a>

<!-- MISSION -->
<div class="abs watermark">HALDEN RIDGE</div>
<div class="abs mission-bar"></div>
<div class="abs camera" role="img" aria-label="Photo of a white bullet security camera on a wall bracket"></div>
<div class="abs pointer"></div>
<div class="abs pointer-dot"></div>
<div class="abs mission">
  <h2>Our <span>Mission</span></h2>
  <p class="lead">To provide our customers with comprehensive security, audio/video, and automation with top notch customer service. We Ensure Security with Smart Tools.</p>
  <p class="body">The graded security measures from Halden Ridge Security ensure the safety of both residential and commercial property. We provide a wide range of Residential and Commercial Security Solutions.</p>
  <a class="btn-dark" style="width:129px;height:43px">LEARN MORE</a>
</div>

<!-- SOLUTIONS -->
<section class="abs solutions"></section>

<article class="abs card" style="top:1697px">
  <div class="card-photo" role="img" aria-label="Photo of a modern commercial office building with glass windows" style="background:linear-gradient(90deg,#1d1d1d 0%,#222 35%,#4a4a4a 55%,#8c8a86 75%,#b6b4b0 100%)"></div>
  <svg class="card-photo" viewBox="0 0 1017 524" preserveAspectRatio="none"><polygon points="587,524 1017,0 1017,524" fill="#d1ad3a" opacity=".82"/></svg>
  <div class="card-copy" style="top:106px">
    <h3>Commercial Solutions</h3>
    <p class="tag">Protect assets and security of your business with Exceptional Commercial Security Installation</p>
    <p>People’s safety is our top priority. This includes ensuring that the security system built at your commercial property is configured accurately. Further, it will protect against intruders, burglaries, and holdups. We do this by:</p>
  </div>
  <a class="btn-dark" style="top:381px">LEARN MORE</a>
</article>

<article class="abs card" style="top:2415px">
  <div class="card-photo" role="img" aria-label="Photo of a bright living room with a wall-mounted screen, chair and plants" style="background:linear-gradient(90deg,#1b1d1f 0%,#25272a 35%,#6e685e 55%,#b7b0a4 75%,#d6d2ca 100%)"></div>
  <svg class="card-photo" viewBox="0 0 1017 522" preserveAspectRatio="none"><polygon points="587,522 1017,0 1017,522" fill="#d1ad3a" opacity=".82"/></svg>
  <div class="card-copy" style="top:98px">
    <h3>Residential Solutions</h3>
    <p class="tag">Consider a home surveillance device that would do more for you and your family than you ever imagined.</p>
    <p>Halden Ridge Security is your trustable security provider. Also, as certified professionals carry out the installation, you have everything under control. Your home is being securely watched from various points, with cameras capable of tracking any intruder’s path.</p>
  </div>
  <a class="btn-dark" style="top:396px">LEARN MORE</a>
</article>

<!-- CTA -->
<section class="abs cta"></section>
<div class="abs cta-photo" role="img" aria-label="Photo of white modern architecture with vertical ribbed structure"></div>
<h2 class="abs cta-title">Interested in knowing more?</h2>
<p class="abs cta-text">Lorem ipsum dolor sit amet, consectetur adipiscing elit, sed do eiusmod tempor incididunt.</p>
<a class="abs btn-outline" style="left:93px;top:3392px;width:248px;height:45px;color:var(--ink)">LEARN MORE RESOURCES</a>
<a class="abs btn-gold" style="left:364px;top:3392px;width:139px;height:45px;font-weight:600">CONTACT</a>

<!-- FOOTER -->
<footer class="abs footer"></footer>
<div class="abs brand" style="left:100px;top:3612px"><span class="brand-dot"></span>Halden Ridge</div>
<a class="abs btn-outline" style="left:970px;top:3611px;width:140px;height:46px;color:#fff;font-size:15px">Request Quote</a>
<div class="abs foot-col" style="left:113px"><h4>ABOUT</h4><ul><li>Our Company</li><li>Members</li></ul></div>
<div class="abs foot-col" style="left:281px"><h4>SOLUTIONS</h4><ul><li>Commercial</li><li>Residential</li></ul></div>
<div class="abs foot-col" style="left:438px"><h4>RESOURCES</h4><ul><li>Packages</li><li>Specials</li></ul></div>
<div class="abs foot-col" style="left:589px"><h4>CONTACT</h4><ul>
  <li><svg width="14" height="11" viewBox="0 0 14 11"><rect x=".7" y=".7" width="12.6" height="9.6" fill="none" stroke="#9a9a9a" stroke-width="1.3"/><path d="M1 1l6 5 6-5" fill="none" stroke="#9a9a9a" stroke-width="1.3"/></svg>info@haldenridge.example</li>
  <li><svg width="13" height="13" viewBox="0 0 24 24"><path fill="#9a9a9a" d="M6.6 10.8a15 15 0 006.6 6.6l2.2-2.2a1 1 0 011-.25 11.4 11.4 0 003.6.57 1 1 0 011 1V20a1 1 0 01-1 1A17 17 0 013 4a1 1 0 011-1h3.5a1 1 0 011 1c0 1.25.2 2.45.57 3.570a1 1 0 01-.25 1z"/></svg>555 014 2290</li>
</ul></div>
<p class="abs copyright">2020 HALDEN RIDGE SECURITY. ALL RIGHTS RESERVED.</p>

</body>
</html>
```